Business Card Needed for Crafter of Pottery, Jewelry and Artwork

Calling all designers in search of an artistic challenge.

I need a new business card design for my pottery, jewelry and artwork business, Woven Glass and Tide, based in Vancouver BC.

I would like a card that is bright and inviting and preferably incorporates my logo and a sample of photos of my work while having a clean fresh look. The following contact details would preferably be included on the card as well:
• Melinda Osgood
• Designer
• Phone: 604.555.0147
• Email: Designer@WovenGlassandTide.example
• Website: www.WovenGlassandTide.example
• Blog: www.KilnNotesDaily.example

The logo is attached in two color schemes in both Vector and Source formats. On past cards I’ve also included photos of my work. By including photos of the work the pieces are showcased and it catches people’s eye and prompts them to pick up the card and look at it more closely. For example, if I leave a stack in a coffee shop I want people to be drawn to the card, to pick it up and get a sense of the my product lines. Please feel free to pull photos of my work directly off of my website. If you need photos with higher pixels please let me know and I’ll email them directly to you. The website background is bffbda (191, 251, 218). I would like the business cards to match the feel of the website for consistency but the cards do not need to use the exact same colors. My website and current business card are predominantly turquoise shades. The background uses stripes provided by the website template. I don’t know the exact colors of the stripes.

My current business card is attached to show the use of photos in a design. Please note that I am not thrilled with my own design and am looking for variations and completely new designs. This example is not meant to be used as a template or starting point.

Here is some background surrounding my company:
WGT offers one of a kind jewelry, pottery, artwork and leather bags each designed with a twist. The pottery varies from rustic every day functional ware to raku artwork. The jewelry ranges from simple sterling every day pieces to multimedia pieces incorporating stone, metal, ceramics and fabric. The artwork is multimedia, typically acrylic paired with a natural element such as bark. All the bags are leather with reworked kimono fabric or patterned silk lining.

Feel free to check out my website to get a flavour for my work and the color scheme I've used on marketing materials so far. www.wovenglassandtide.example
Updates

Thank you to everyone who has submitted a design so far. I hope everyone has received some helpful feedback.

I'm going to post a survey to customers and friends asking for their votes. If you have new designs to submit please try to get them in by Saturday March 30 at noon so that I can include it in the survey launch.

Thank you

Target Market(s)

Females aged 25-65 interested in one of a kind functional pottery and jewelry.

Industry/Entity Type

Coffee Shop

Requirements
Must have
• Contact information, website, blog
Nice to have
• Logo, photos

```html
<!DOCTYPE html>
<html lang="en">
<head>
<meta charset="utf-8">
<title>Woven Glass and Tide – Business Card</title>
<link rel="stylesheet" href="https://fonts.googleapis.com/css2?family=Crimson+Pro:wght@400;600;700&display=swap">
<style>
  :root {
    --navy: #1f1f5e;
    --royal: #3434a4;
    --turquoise: #4cc4b4;
    --paper: #ffffff;
    --backdrop: #eef1f0;
    --ink: #111111;
    --photo-mugs: #7fa6a0;
    --photo-plate: #a9bba0;
    --photo-necklace: #c98f80;
    --photo-jar: #2f4f93;
    --photo-earrings: #4a3a30;
    --photo-bag: #c94a4a;
  }
  * { margin: 0; padding: 0; box-sizing: border-box; }
  html, body { width: 1200px; height: 1005px; overflow: hidden; }
  body {
    position: relative;
    background: var(--backdrop);
    font-family: "Crimson Pro", Georgia, serif;
    color: var(--navy);
  }

  /* ---------- front card ---------- */
  .card-front {
    position: absolute;
    left: 35px; top: 40px;
    width: 792px; height: 450px;
    background: var(--paper);
    border-radius: 30px;
    overflow: hidden;
  }
  .brand {
    position: absolute;
    display: flex; align-items: center; justify-content: center; gap: 14px;
    font-weight: 600;
    color: var(--navy);
    white-space: nowrap;
  }
  .brand-dot {
    width: 18px; height: 18px; border-radius: 50%;
    background: var(--turquoise);
    flex: none;
  }
  .card-front .brand {
    left: 0; width: 792px; top: 112px; font-size: 38px;
  }
  .holder {
    position: absolute;
    left: 0; width: 792px; top: 264px;
    text-align: center;
    font-size: 29px; font-weight: 700;
  }
  .holder .role { font-weight: 400; font-size: 25px; color: var(--royal); }
  .band { position: absolute; left: 0; top: 0; }
  .contacts {
    position: absolute; left: 0; width: 792px;
    color: var(--paper);
    font-size: 20px;
    display: flex; justify-content: center; align-items: center; gap: 10px;
    white-space: nowrap;
  }
  .contacts.row-one { top: 372px; }
  .contacts.row-two { top: 410px; }
  .contacts svg { width: 16px; height: 16px; flex: none; }
  .blog-mark {
    width: 16px; height: 16px; border-radius: 3px;
    background: #f08a3a; flex: none;
  }

  /* ---------- back card ---------- */
  .card-back {
    position: absolute;
    left: 360px; top: 520px;
    width: 790px; height: 450px;
    background: var(--paper);
    border: 1.5px solid var(--ink);
    border-radius: 30px;
  }
  .work-photo {
    position: absolute;
    width: 200px; height: 134px;
    border: 2px solid var(--ink);
    border-radius: 18px;
  }
  .col-left { left: 24px; }
  .col-right { left: 567px; }
  .row-a { top: 11px; }
  .row-b { top: 157px; }
  .row-c { top: 305px; }
  .mugs { background: linear-gradient(180deg, #dfe6e4 0%, var(--photo-mugs) 55%, #3b3f40 100%); }
  .plate { background: radial-gradient(ellipse at center, #8fbfa8 0%, var(--photo-plate) 55%, #c7ad86 100%); }
  .necklace { background: linear-gradient(180deg, #e8e2dc 0%, var(--photo-necklace) 60%, #d9cfc5 100%); }
  .jar { background: radial-gradient(ellipse at 50% 55%, #4d6fb5 0%, var(--photo-jar) 60%, #e6e2da 100%); }
  .earrings { background: linear-gradient(135deg, #2b1e18 0%, var(--photo-earrings) 50%, #e27a95 100%); }
  .bag { background: linear-gradient(180deg, #eeeeee 0%, var(--photo-bag) 40%, #b43c3c 100%); }

  .card-back .brand {
    left: 250px; width: 290px; top: 185px; font-size: 30px;
  }
  .card-back .web {
    position: absolute; left: 230px; width: 330px; top: 345px;
    text-align: center; font-size: 21px; color: var(--ink);
  }
</style>
</head>
<body>

<section class="card-front">
  <div class="brand"><span class="brand-dot"></span>Woven Glass and Tide</div>

  <p class="holder">Melinda Osgood, <span class="role">Designer</span></p>

  <svg class="band" width="792" height="450" viewBox="0 0 792 450" aria-hidden="true">
    <path d="M0 400 Q396 220 792 400 L792 450 L0 450 Z" fill="var(--navy)"/>
    <path d="M0 392 Q396 210 792 392" fill="none" stroke="var(--royal)" stroke-width="3"/>
  </svg>

  <div class="contacts row-one">
    <svg viewBox="0 0 16 16" aria-hidden="true"><path d="M4 1.5c.6 0 2 2.6 2 3.2 0 .6-1.2 1-1.2 1.6 0 .9 2.6 3.6 3.6 3.6.6 0 1-1.2 1.6-1.2.6 0 3.2 1.4 3.2 2 0 1-1.5 3.1-3 3.1C6.3 13.8 2.2 9.7 2.2 5c0-1.5 1-3.5 1.8-3.5z" fill="#fff"/></svg>
    <span>604.555.0147</span>
    <svg viewBox="0 0 16 16" aria-hidden="true"><rect x="1" y="3.5" width="14" height="9.5" rx="1.5" fill="#fff"/><path d="M1.5 4.5 8 9l6.5-4.5" fill="none" stroke="var(--navy)" stroke-width="1.3"/></svg>
    <span>Designer@WovenGlassandTide.example</span>
  </div>
  <div class="contacts row-two">
    <svg viewBox="0 0 16 16" aria-hidden="true"><circle cx="8" cy="8" r="6.5" fill="none" stroke="#fff" stroke-width="1.4"/><ellipse cx="8" cy="8" rx="2.8" ry="6.5" fill="none" stroke="#fff" stroke-width="1.2"/><path d="M1.5 8h13M2.6 4.6h10.8M2.6 11.4h10.8" stroke="#fff" stroke-width="1"/></svg>
    <span>www.WovenGlassandTide.example</span>
    <span class="blog-mark"></span>
    <span>www.KilnNotesDaily.example</span>
  </div>
</section>

<section class="card-back">
  <div class="work-photo col-left row-a mugs" role="img" aria-label="Photo of three turquoise glazed pottery mugs"></div>
  <div class="work-photo col-left row-b plate" role="img" aria-label="Photo of a green glazed pierced ceramic plate"></div>
  <div class="work-photo col-left row-c necklace" role="img" aria-label="Photo of a pink stone bead necklace with copper pendant"></div>
  <div class="work-photo col-right row-a jar" role="img" aria-label="Photo of a speckled blue lidded pottery jar"></div>
  <div class="work-photo col-right row-b earrings" role="img" aria-label="Photo of pink bead and sea glass earrings on bark"></div>
  <div class="work-photo col-right row-c bag" role="img" aria-label="Photo of a red leather tote bag with black straps"></div>

  <div class="brand"><span class="brand-dot"></span>Woven Glass and Tide</div>
  <p class="web">www.WovenGlassandTide.example</p>
</section>

</body>
</html>
```